Guarenteed! - Homepage Website Design - Coding not required- Winner to complete further pages

Hi all,

We're looking at redesigning our current website with a few adjustments to other pages but the main adjustments will be on the homepage which is what this design request is for. Please note : any of these ideas can be changed if you have something particularly different / special in mind etc.

P.S Coding is not required, just a design.

- Our website -

Our website is simply a price comparison website that allows customers to find companies within their area at the best price. The products available are mostly related to the vehicle trade and all refer to vinyl. This includes the likes of vehicle window tint, vehicle colour change vehicle wrap, vehicle signage as well as other cosmetic vinyl modifications. We allow the customer to search for their product within their chosen area and receive a list of companies who supply their product within that area. From here they can compare prices and view further details on the company.

- What we're looking to do -

We're looking first of all to adjust how the website homepage is displayed, this includes adding images and adjusting the colours that are explained below:

First of all, we look to spread out each of the 12 products (which can be seen on the website as it stands) and add an image to each of the products (all being spaced out as shown in our sketch)

We've been told the website looks too busy so we're thinking if we adjust the colours to more simplier neutral colours as well as the main focus of the website being on the 12 images, that would be great.

- Logo + Banner -

Logo to remain top left although banner may be removed / adjusted to make simplier.

- Colours -

Adjustments - Colours shades
We want the website to still look exciting but simplify the colours. Needs to be kept up to date with the colours / textures etc (bright colours to highlight keypoints)
We're still looking to use either blue or orange or maybe both to highlight these keypoints but the main website to be light colours and maybe even black on white background. The entire homepage can be adjusted colour wise if you feel it fits into your theme including menu bars, banners etc. The key is to get this right with being not too overpowering with the colours but still look interesting and up to date.

- 1 - 4 steps banner - (text may change)

This sits just under the logo and explains to the user how easy the website is to use and the steps they need to take. This may change to a 1 - 5 steps but we're looking to have this designed once the overall colours / theme of the website is sorted.

- 12 images - 4 x 3

This is the main focus of the website and will be the main focus of what the customer sees first of all. This will be where they select their product and then underneath, enter their postcode and distance they would like to search within. As explained further up, we have some of the product images available so if you can where possible add these to the design and then duplicate the images on those we currently don't have available.

- 12 Images -Titles -

These titles will be in this order from left to right and etc

- Colour Change Wrap
- Printed Vehicle Wrap
- Window Tint
- Headlight Tint
- Vehicle Signage
- Shop Signage
- Roof Vinyl Wrap
- Bonnet Vinyl Wrap
- Carbon Fibre Vinyl
- Stickerbomb Vinyl
- Clear Protective Vinyl
- Wheel Refurb

Text to be quite large, centered and with the o to the left of the title. Short titles like 'Window Tint' should fit on one line in the middle of the box where as titles such as ' Stickerbomb Vinyl Wrap' should have the 'Stickerbomb Vinyl' on the first line with the 'Wrap' on the line below. The background of this text is up to experient, might be worth just a simple colour or it might be worth using a bright blue or orange to keep in with the theme of the logo etc.

These will also have the circle tick box to the left of the title (as on the current website) where the customer clicks to select the product they have available.
We were also thinking that if when the customer ticks the circle on their selected box, the box is highlighted in some way to show this.

- Search Block -

This will appear under the 12 images and allows the customer to input their postcode and distance for the search criteria. Colours on this can of course be adjusted to keep in theme with the website.

- Under the 12 Images -

- Block underneath the 12 images and search block -

To the left will be some key bullet points about the website - maybe 4 or 5 with a green tick to the left of this. Background colour will probably be best to be a light colour, possibly grey.

Then to the right of this will appear 4 images, 2 before and 2 after when applying these products. Images to be used aren't fully decided on and we would like this stage of the design left to the end when the rest of the theme etc have been decided on.

Attached images are as follows :
- How the website looks as it stands
- The fold line on the website (obviously important)
- Our rough sketch of how we'd like the website homepage to look.
- We have 7 of the images ready that are all attached in this one file. Please duplicate the images on those that currently don't have the image available.

We will also be requesting a website developer to put this into action if our current designer falls through so please feel free to contact us if potentially interested.

The layout can change if you can think of something particular different / unique that works with this design. The main idea is to not only get the 12 products on view to the viewers but also the keypoints and before and after images.

Any questions, please ask away as we're bound to have forgotten a few things.

Thanks and good luck!

Hi all, keep the designs coming.

We haven't quite seen that extra special design we're after. As stated, we're after something fairly simple to suit the youth as well as the middle aged but we're also after something that bit special.

Colours to concentrate on are still and orange etc although feel free to use other colours if you have anything special in mind.

Please experience and we'll give you our honest feedback.

Many thanks all and good luck!

Hi all, this is a message to all the designers.

Some good designs coming in but we're still after that something special for the website design. Keep the designs coming and please feel free to experiment with the design colours, layout etc.

The basic principle of the website needs to remain regarding the 12 products, search within block and 4 steps all appearing on the homepage.

The 4 steps seems to work best when it's got text as well as some simple images next to this.

A variation with the product titles with how to display this, some designers have gone with a simple white background whereas others have gone with colours. Please experiment here and where possible, add a contract / texture to the colour. Please remember the product titles needs to be clear, centured and with the circle tick box to the left of it. 

We're after a fairly simple design although we need it to look 21st century, up to date as well as interesting. The key points straight away are the 4 steps as well as the 12 products so try to guide the viewer to these areas a little.

White background behind the 12 images seems to be a much, although a light colour could possibly work.

The keypoints underneath these 12 products are too very important as it outlines what we do etc. Tick colour can vary.

Next to these keypoints will be the 'before' and 'after' images, these images needs to be fairly small and ensure there is white background around the image itself.

Good luck all and any questions, feel free to ask away.

Thanks!

Hi,

 Thank you for your time and effort with these designs, we are very nearly there with the design but we've thought of something that may work for the homepage. A curved arrow from step 1 pointing to the products, this may or may not work but feel free to give it a go.

Many thanks,

Thank you to everyone for your time and efforts with the design. It's hugely appreciated so thank you all once again.

Wish you all the luck in the future.

```html
<!DOCTYPE html>
<html lang="en">
<head>
<meta charset="utf-8">
<title>WrapScout – Compare Vinyl Installers</title>
<link rel="stylesheet" href="https://fonts.googleapis.com/css2?family=Oswald:wght@600;700&family=Roboto+Condensed:wght@400;700&family=Open+Sans:wght@400;600&family=Roboto:wght@400;700&display=swap">
<style>
  :root{
    --navy:#2d4a86;
    --navy-dark:#213a6e;
    --label:#33416f;
    --orange:#e8801e;
    --orange-dark:#c9650e;
    --teal:#1f8f8c;
    --teal-light:#2aa9a3;
    --teal-tab:#1fb39b;
    --grey-mid:#7d7d7d;
    --grey-dark:#4a4a4a;
    --charcoal:#333333;
    --white:#ffffff;
  }
  *{box-sizing:border-box;margin:0;padding:0}
  html,body{width:686px;height:1200px;overflow:hidden;background:var(--white)}
  body{position:relative;font-family:"Open Sans",sans-serif}
  .abs{position:absolute}

  /* header */
  .site-header{left:0;top:0;width:686px;height:72px;background:linear-gradient(#fafafa,#e9e9e9)}
  .brand{left:86px;top:22px;display:flex;align-items:center;gap:7px}
  .brand-dot{width:26px;height:26px;border-radius:50%;background:var(--orange)}
  .brand-name{font-family:"Roboto Condensed",sans-serif;font-weight:700;font-size:24px;line-height:26px;color:var(--navy);letter-spacing:.3px}
  .promo{left:290px;top:4px;width:316px;height:65px;background:linear-gradient(#f39a2c,var(--orange-dark));border-radius:2px;overflow:hidden}
  .promo-ribbon{left:6px;top:4px;width:296px;height:20px;background:var(--navy);color:var(--white);font-family:"Roboto Condensed",sans-serif;font-weight:700;font-size:12.5px;text-align:center;line-height:20px;letter-spacing:.4px}
  .promo-line{left:8px;top:33px;color:var(--white);font-family:"Roboto",sans-serif;font-weight:400;font-size:13px}
  .promo-line b{font-size:18px;font-weight:700}
  .promo-map{left:214px;top:26px;width:98px;height:37px;background:linear-gradient(135deg,#eadfb8,#c9d6a8);border-radius:2px}

  /* nav */
  .main-nav{left:0;top:72px;width:686px;height:26px;background:linear-gradient(#3a5a9a,var(--navy-dark));display:flex;align-items:center;padding-left:69px}
  .main-nav a{font-family:"Roboto Condensed",sans-serif;font-size:11.5px;color:var(--white);text-decoration:none;padding:0 11px;height:26px;line-height:26px;border-right:1px solid rgba(255,255,255,.18)}
  .social{top:75px;width:19px;height:19px;border-radius:2px}
  .social.one{left:564px;background:#3b5998}
  .social.two{left:586px;background:#2fa9e0}

  /* steps */
  .how-it-works{left:0;top:98px;width:686px;height:180px;background:radial-gradient(ellipse at 50% 30%,#fbfbfb,#dcdcdc)}
  .section-title{left:0;top:110px;width:686px;text-align:center;font-family:"Oswald",sans-serif;font-weight:700;font-size:15px;color:var(--grey-dark);letter-spacing:1px}
  .step{top:140px;width:134px;text-align:center}
  .step-badge{margin:0 auto;width:34px;height:34px;position:relative}
  .step-badge svg{position:absolute;left:0;top:0}
  .step-badge span{position:relative;line-height:34px;font-family:"Roboto",sans-serif;font-size:10px;color:var(--white);font-weight:700}
  .step-icon{margin:10px auto 0;width:40px;height:38px}
  .step-text{margin-top:6px;font-family:"Roboto Condensed",sans-serif;font-size:10.5px;line-height:12px;color:var(--label)}
  .step-text.grey{color:var(--grey-mid)}
  .steps-shadow{left:80px;top:276px;width:526px;height:6px;background:radial-gradient(ellipse at 50% 0,rgba(0,0,0,.25),transparent 70%)}

  /* products */
  .product{width:124px;text-align:center}
  .product-photo{width:124px}
  .product-label{font-family:"Roboto Condensed",sans-serif;font-size:10px;line-height:11px;color:var(--label);margin-top:10px}

  /* keypoints */
  .keypoints-band{left:0;top:788px;width:686px;height:227px;background:radial-gradient(ellipse at 30% 50%,var(--teal-light),var(--teal))}
  .keypoints{left:94px;top:847px;list-style:none}
  .keypoints li{display:flex;align-items:center;gap:10px;height:27px;font-size:10px;color:var(--white)}
  .compare-card{top:752px;width:127px;height:268px;background:var(--white);box-shadow:0 1px 4px rgba(0,0,0,.3);border-radius:2px}
  .compare-tab{position:absolute;left:3px;top:3px;width:121px;height:28px;color:var(--white);font-family:"Roboto",sans-serif;font-size:16px;text-align:center;line-height:28px;border-radius:2px}
  .compare-tab::after{content:"";position:absolute;left:54px;bottom:-6px;border:6px solid transparent;border-bottom:0;border-top-color:inherit}
  .tab-before{background:var(--teal-tab);border-color:var(--teal-tab)}
  .tab-after{background:var(--orange);border-color:var(--orange)}
  .hex{position:absolute;left:16px;width:94px;height:100px;clip-path:polygon(50% 0,100% 25%,100% 75%,50% 100%,0 75%,0 25%)}

  /* footer */
  .site-footer{left:0;top:1052px;width:686px;height:148px;background:var(--charcoal)}
  .zigzag{left:0;top:1046px}
  .footer-title{left:0;top:1086px;width:686px;text-align:center;font-family:"Roboto",sans-serif;font-weight:400;font-size:17px;color:var(--white)}
  .field{top:1120px;width:124px;height:25px;background:var(--white);font-size:8px;color:#888;padding-left:8px;line-height:25px}
  .submit{left:445px;top:1120px;width:54px;height:25px;background:var(--orange);color:var(--white);font-family:"Roboto Condensed",sans-serif;font-weight:700;font-size:11px;text-align:center;line-height:25px}
  .copyright{left:0;top:1163px;width:686px;text-align:center;font-size:6.5px;color:#cfcfcf}
</style>
</head>
<body>

<header class="abs site-header"></header>
<div class="abs brand"><span class="brand-dot"></span><span class="brand-name">WRAPSCOUT</span></div>
<div class="abs promo">
  <div class="abs promo-ribbon">FIND A PROFESSIONAL VINYL INSTALLER TODAY</div>
  <div class="abs promo-line">Search Save in <b>Seconds!</b></div>
  <div class="abs promo-map" role="img" aria-label="Map of towns with location pin"></div>
</div>

<nav class="abs main-nav">
  <a href="#">HOME</a><a href="#">ABOUT US</a><a href="#">CONTACT US</a><a href="#">BLOG</a><a href="#">LIST YOUR COMPANY HERE</a>
</nav>
<span class="abs social one"></span><span class="abs social two"></span>

<section class="abs how-it-works"></section>
<h2 class="abs section-title">HOW IT WORKS</h2>

<div class="abs step" style="left:75px">
  <div class="step-badge"><svg width="34" height="34" viewBox="0 0 34 34"><polygon points="17,0 22,7 31,5 29,13 34,17 29,21 31,29 22,27 17,34 12,27 3,29 5,21 0,17 5,13 3,5 12,7" fill="#e8801e"/></svg><span>1</span></div>
  <svg class="step-icon" viewBox="0 0 40 38"><path d="M8 16 L12 6 H28 L32 16 H36 V30 H31 V35 H25 V30 H15 V35 H9 V30 H4 V16Z" fill="#2d4a86"/><rect x="14" y="9" width="12" height="6" fill="#e6e6e6"/><circle cx="11" cy="22" r="3" fill="#e6e6e6"/><circle cx="29" cy="22" r="3" fill="#e6e6e6"/></svg>
  <div class="step-text">SELECT CHOSEN<br>PRODUCT</div>
</div>
<div class="abs step" style="left:209px">
  <div class="step-badge"><svg width="34" height="34" viewBox="0 0 34 34"><polygon points="17,0 22,7 31,5 29,13 34,17 29,21 31,29 22,27 17,34 12,27 3,29 5,21 0,17 5,13 3,5 12,7" fill="#666"/></svg><span>2</span></div>
  <svg class="step-icon" viewBox="0 0 40 38"><circle cx="17" cy="15" r="11" fill="none" stroke="#444" stroke-width="5"/><circle cx="17" cy="15" r="3" fill="#444"/><line x1="25" y1="23" x2="34" y2="34" stroke="#444" stroke-width="6" stroke-linecap="round"/></svg>
  <div class="step-text grey">INPUT POSTCODE,<br>DISTANCE + SEARCH</div>
</div>
<div class="abs step" style="left:343px">
  <div class="step-badge"><svg width="34" height="34" viewBox="0 0 34 34"><polygon points="17,0 22,7 31,5 29,13 34,17 29,21 31,29 22,27 17,34 12,27 3,29 5,21 0,17 5,13 3,5 12,7" fill="#666"/></svg><span>3</span></div>
  <svg class="step-icon" viewBox="0 0 40 38"><rect x="12" y="12" width="18" height="11" fill="#444"/><rect x="15" y="15" width="12" height="5" fill="#e6e6e6"/><path d="M8 10 A14 14 0 0 1 30 5 L33 2 L34 12 L24 11 L27 8 A10 10 0 0 0 11 12Z" fill="#444"/><path d="M32 26 A14 14 0 0 1 10 32 L7 35 L6 25 L16 26 L13 29 A10 10 0 0 0 29 24Z" fill="#444"/></svg>
  <div class="step-text grey">COMPARE COMPANIES<br>+ PRICES</div>
</div>
<div class="abs step" style="left:477px">
  <div class="step-badge"><svg width="34" height="34" viewBox="0 0 34 34"><polygon points="17,0 22,7 31,5 29,13 34,17 29,21 31,29 22,27 17,34 12,27 3,29 5,21 0,17 5,13 3,5 12,7" fill="#666"/></svg><span>4</span></div>
  <svg class="step-icon" viewBox="0 0 40 38"><path d="M12 3 L17 11 L13 15 C15 21 19 25 24 27 L28 23 L36 28 L32 35 C20 34 7 22 6 8Z" fill="#444"/></svg>
  <div class="step-text grey">CONTACT CHOSEN<br>COMPANY</div>
</div>
<div class="abs steps-shadow"></div>

<div class="abs product" style="left:81px;top:310px"><div class="product-photo" style="height:86px;background:linear-gradient(160deg,#d4272b,#9e1619)" role="img" aria-label="Red car with colour change wrap"></div><div class="product-label">COLOUR CHANGE<br>WRAP</div></div>
<div class="abs product" style="left:214px;top:310px"><div class="product-photo" style="height:86px;background:linear-gradient(180deg,#8fb3dc 0,#8fb3dc 45%,#4f8f3a 45%,#3f7a2e)" role="img" aria-label="Van with printed vehicle wrap"></div><div class="product-label">PRINTED VEHICLE<br>WRAP</div></div>
<div class="abs product" style="left:348px;top:310px"><div class="product-photo" style="height:86px;background:linear-gradient(160deg,#4cc23a,#2b8a22)" role="img" aria-label="Green hatchbacks with tinted windows"></div><div class="product-label" style="margin-top:16px">WINDOW TINT</div></div>
<div class="abs product" style="left:482px;top:310px"><div class="product-photo" style="height:86px;background:linear-gradient(160deg,#c9ced8,#8d96a8)" role="img" aria-label="Silver car front with tinted headlights"></div><div class="product-label" style="margin-top:16px">HEADLIGHT TINT</div></div>

<div class="abs product" style="left:81px;top:452px"><div class="product-photo" style="height:101px;background:linear-gradient(160deg,#eef0f2,#c3c8cd)" role="img" aria-label="White van with company signage"></div><div class="product-label">VEHICLE SIGNAGE</div></div>
<div class="abs product" style="left:214px;top:452px"><div class="product-photo" style="height:101px;background:linear-gradient(180deg,#d9d9d9 0,#d9d9d9 12%,#2f2f2f 12%,#3b3b3b)" role="img" aria-label="Shop front with vinyl signage"></div><div class="product-label">SHOP SIGNAGE</div></div>
<div class="abs product" style="left:348px;top:452px"><div class="product-photo" style="height:101px;background:linear-gradient(160deg,#d2d2d2,#8a8a8a)" role="img" aria-label="Silver car with black roof wrap"></div><div class="product-label" style="margin-top:4px">ROOF VINYL<br>WRAP</div></div>
<div class="abs product" style="left:482px;top:452px"><div class="product-photo" style="height:101px;background:linear-gradient(160deg,#cfcfcf,#7e7e7e)" role="img" aria-label="Silver car with black bonnet wrap"></div><div class="product-label" style="margin-top:4px">BONNET VINYL<br>WRAP</div></div>

<div class="abs product" style="left:81px;top:603px"><div class="product-photo" style="height:101px;background:linear-gradient(160deg,#3a3d41,#1c1c1c)" role="img" aria-label="Car interior trimmed in carbon fibre vinyl"></div><div class="product-label" style="margin-top:5px">CARBON FIBRE<br>VINYL</div></div>
<div class="abs product" style="left:214px;top:603px"><div class="product-photo" style="height:101px;background:linear-gradient(180deg,#e39238 0,#d9b23c 55%,#e4e4e4 55%,#cfcfcf)" role="img" aria-label="White car bonnet covered in stickerbomb vinyl"></div><div class="product-label" style="margin-top:5px">STICKERBOMB<br>VINYL</div></div>
<div class="abs product" style="left:348px;top:603px"><div class="product-photo" style="height:101px;background:linear-gradient(160deg,#6d66b0,#2b2660)" role="img" aria-label="Clear protective film being applied to a car"></div><div class="product-label" style="margin-top:5px">CLEAR PROTECTIVE<br>VINYL</div></div>
<div class="abs product" style="left:482px;top:603px"><div class="product-photo" style="height:101px;background:linear-gradient(160deg,#b8b8b8,#4a4540)" role="img" aria-label="Refurbished alloy wheel"></div><div class="product-label" style="margin-top:11px">WHEEL REFURB</div></div>

<section class="abs keypoints-band"></section>
<ul class="abs keypoints">
  <li><svg width="17" height="13" viewBox="0 0 17 13"><path d="M1 7 L6 12 L16 2 L13 0 L6 7 L4 4Z" fill="#a8ece3"/></svg>Lorem ipsum dolor sit amet</li>
  <li><svg width="17" height="13" viewBox="0 0 17 13"><path d="M1 7 L6 12 L16 2 L13 0 L6 7 L4 4Z" fill="#a8ece3"/></svg>Curabitur non nisi at dui posuere iaculis.</li>
  <li><svg width="17" height="13" viewBox="0 0 17 13"><path d="M1 7 L6 12 L16 2 L13 0 L6 7 L4 4Z" fill="#a8ece3"/></svg>Mauris fermentum sem ut vehicula pharetra.</li>
  <li><svg width="17" height="13" viewBox="0 0 17 13"><path d="M1 7 L6 12 L16 2 L13 0 L6 7 L4 4Z" fill="#a8ece3"/></svg>Quisque quis felis ac diam feugiat pharetra.</li>
</ul>

<div class="abs compare-card" style="left:345px">
  <div class="compare-tab tab-before">Before</div>
  <div class="hex" style="top:46px;background:linear-gradient(160deg,#dfe0e4,#8e929a)" role="img" aria-label="Car door before vinyl"></div>
  <div class="hex" style="top:152px;background:linear-gradient(160deg,#a9a9a9,#2e2e2e)" role="img" aria-label="Wheel before refurb"></div>
</div>
<div class="abs compare-card" style="left:480px">
  <div class="compare-tab tab-after">After</div>
  <div class="hex" style="top:46px;background:linear-gradient(160deg,#e9eaec,#a5a8ad)" role="img" aria-label="Car door after vinyl"></div>
  <div class="hex" style="top:152px;background:linear-gradient(160deg,#c9ced6,#2a2a2a)" role="img" aria-label="Wheel after refurb"></div>
</div>

<footer class="abs site-footer"></footer>
<svg class="abs zigzag" width="686" height="8" viewBox="0 0 686 8" preserveAspectRatio="none"><path d="M0 8 L0 6 L5 2 L10 6 L15 2 L20 6 L25 2 L30 6 L35 2 L40 6 L45 2 L50 6 L55 2 L60 6 L65 2 L70 6 L75 2 L80 6 L85 2 L90 6 L95 2 L100 6 L105 2 L110 6 L115 2 L120 6 L125 2 L130 6 L135 2 L140 6 L145 2 L150 6 L155 2 L160 6 L165 2 L170 6 L175 2 L180 6 L185 2 L190 6 L195 2 L200 6 L205 2 L210 6 L215 2 L220 6 L225 2 L230 6 L235 2 L240 6 L245 2 L250 6 L255 2 L260 6 L265 2 L270 6 L275 2 L280 6 L285 2 L290 6 L295 2 L300 6 L305 2 L310 6 L315 2 L320 6 L325 2 L330 6 L335 2 L340 6 L345 2 L350 6 L355 2 L360 6 L365 2 L370 6 L375 2 L380 6 L385 2 L390 6 L395 2 L400 6 L405 2 L410 6 L415 2 L420 6 L425 2 L430 6 L435 2 L440 6 L445 2 L450 6 L455 2 L460 6 L465 2 L470 6 L475 2 L480 6 L485 2 L490 6 L495 2 L500 6 L505 2 L510 6 L515 2 L520 6 L525 2 L530 6 L535 2 L540 6 L545 2 L550 6 L555 2 L560 6 L565 2 L570 6 L575 2 L580 6 L585 2 L590 6 L595 2 L600 6 L605 2 L610 6 L615 2 L620 6 L625 2 L630 6 L635 2 L640 6 L645 2 L650 6 L655 2 L660 6 L665 2 L670 6 L675 2 L680 6 L686 2 L686 8Z" fill="#333"/></svg>
<h3 class="abs footer-title">Join Our Mailing List</h3>
<div class="abs field" style="left:187px">Your name...</div>
<div class="abs field" style="left:316px">Your email...</div>
<div class="abs submit">SUBMIT</div>
<p class="abs copyright">Copyright © 2013 WrapScout.</p>

</body>
</html>
```